Business cards for our company

We are a new online eLearning company. We create training for organizations that need to comply with governmental regulations. Our courses are built around the concept of an online show so our course has a media player / control bar across the bottom of all courses. We think this is an important element to work into the design. We have a simple mock up which we don't want anyone to just follow but just to give some idea of how the control bar could be used in the design but we are open to anything creative. If you choose to use the control bar, it doesn't have to be used literally. You can add/move/change buttons to suite your design concept. I have most of these files as PSD files so if you, need those just ask and I will post. The font in the course is Open Sans.
Also attached are the logo design and specs.

Target Market(s)

US corporations. Buyers are Senior HR executives, Chief Compiance Officer and General Counsels

Industry/Entity Type

Business

Contact Information for Business Card

Standard size cards. If it helps make the design more impactful, we'll do raised lettering

Font styles to use
Other font styles liked:
• Open Sans

Requirements
Must have
• must use our icon and logo using the supplied standards. needs to include our tag line as shown on the Word document (open to suggestions there as well). Should visually communicate that we are a next-generation eLearning company and not creating the same-old powerpoint looking, click next, click next type of training.

```html
<!DOCTYPE html>
<html lang="en">
<head>
<meta charset="utf-8">
<title>Veralign Business Cards</title>
<link rel="stylesheet" href="https://fonts.googleapis.com/css2?family=Open+Sans:wght@400;600;700&display=swap">
<style>
  :root {
    --page-bg: #e9eaec;
    --brand-blue: #2a72b8;
    --brand-deep: #2567ad;
    --brand-sky: #10a8e2;
    --panel-blue: #2d7cc6;
    --card-white: #ffffff;
    --ink-white: #ffffff;
    --shadow: rgba(0, 0, 0, 0.22);
  }
  * { margin: 0; padding: 0; box-sizing: border-box; }
  html, body {
    width: 1200px;
    height: 950px;
    overflow: hidden;
    background: var(--page-bg);
    font-family: "Open Sans", Arial, sans-serif;
  }
  .canvas {
    position: relative;
    width: 1200px;
    height: 950px;
  }
  .card {
    position: absolute;
    width: 700px;
    height: 400px;
    border-radius: 4px;
    overflow: hidden;
    box-shadow: 0 14px 30px var(--shadow);
  }

  /* Back of card */
  .card-back {
    left: 80px;
    top: 50px;
    background: var(--brand-blue);
    color: var(--ink-white);
  }
  .card-back .wordmark {
    position: absolute;
    left: 140px;
    top: 148px;
    display: flex;
    align-items: center;
    gap: 22px;
  }
  .card-back .mark-square {
    width: 78px;
    height: 78px;
    border-radius: 16px;
    background: var(--card-white);
  }
  .card-back .brand-name {
    font-size: 54px;
    font-weight: 600;
    letter-spacing: 3px;
    color: var(--ink-white);
    text-transform: uppercase;
  }
  .card-back .tagline {
    position: absolute;
    left: 0;
    right: 0;
    top: 290px;
    text-align: center;
    font-size: 16px;
    font-weight: 600;
    padding-left: 120px;
  }

  /* Front of card */
  .card-front {
    left: 420px;
    top: 500px;
    background: var(--card-white);
  }
  .card-front .bands {
    position: absolute;
    inset: 0;
  }
  .card-front .wordmark {
    position: absolute;
    left: 70px;
    top: 70px;
    display: flex;
    align-items: center;
    gap: 22px;
  }
  .card-front .mark-square {
    width: 84px;
    height: 84px;
    border-radius: 16px;
    background: var(--brand-sky);
  }
  .card-front .brand-name {
    font-size: 56px;
    font-weight: 600;
    letter-spacing: 3px;
    color: var(--brand-deep);
    text-transform: uppercase;
  }
  .holder {
    position: absolute;
    left: 420px;
    width: 280px;
    top: 248px;
    text-align: center;
    color: var(--ink-white);
  }
  .holder .name {
    font-size: 24px;
    font-weight: 700;
    letter-spacing: 0.5px;
    text-transform: uppercase;
  }
  .holder .role {
    font-size: 16px;
    font-weight: 400;
    margin-top: 2px;
  }
  .contact-list {
    position: absolute;
    left: 30px;
    top: 270px;
    list-style: none;
    color: var(--ink-white);
    font-size: 17px;
    line-height: 28px;
  }
  .contact-list li {
    display: flex;
    align-items: center;
    gap: 10px;
  }
  .contact-list svg {
    width: 16px;
    height: 16px;
    flex: none;
  }
</style>
</head>
<body>
<main class="canvas">

  <section class="card card-back" aria-label="Card back">
    <div class="wordmark">
      <span class="mark-square" aria-hidden="true"></span>
      <span class="brand-name">Veralign</span>
    </div>
    <p class="tagline">Regulatory Learning Reimagined</p>
  </section>

  <section class="card card-front" aria-label="Card front">
    <svg class="bands" viewBox="0 0 700 400" width="700" height="400" aria-hidden="true">
      <rect class="band-sky" x="0" y="250" width="700" height="150" fill="var(--brand-sky)"/>
      <polygon class="band-panel" points="368,200 700,200 700,400 408,400" fill="var(--panel-blue)"/>
      <line class="band-divider" x1="368" y1="200" x2="408" y2="400" stroke="var(--card-white)" stroke-width="3"/>
    </svg>

    <div class="wordmark">
      <span class="mark-square" aria-hidden="true"></span>
      <span class="brand-name">Veralign</span>
    </div>

    <div class="holder">
      <p class="name">Dana Whitford</p>
      <p class="role">CEO</p>
    </div>

    <ul class="contact-list">
      <li>
        <svg viewBox="0 0 16 16" aria-hidden="true"><path d="M2 5c0-2 2-3 6-3s6 1 6 3l-3 1-1-2H6L5 6 2 5zM4 7h8l2 7H2l2-7zm4 1.5a2 2 0 1 0 0 4 2 2 0 0 0 0-4z" fill="#fff"/></svg>
        <span>212-555-0147</span>
      </li>
      <li>
        <svg viewBox="0 0 16 16" aria-hidden="true"><rect x="4" y="1" width="8" height="14" rx="1.5" fill="none" stroke="#fff" stroke-width="1.6"/><circle cx="8" cy="12.5" r="0.9" fill="#fff"/></svg>
        <span>212-555-0147</span>
      </li>
      <li>
        <svg viewBox="0 0 16 16" aria-hidden="true"><rect x="1.5" y="3.5" width="13" height="9" fill="none" stroke="#fff" stroke-width="1.5"/><path d="M1.5 3.5 8 9l6.5-5.5" fill="none" stroke="#fff" stroke-width="1.5"/></svg>
        <span>Dana.Whitford@Veralign.com</span>
      </li>
      <li>
        <svg viewBox="0 0 16 16" aria-hidden="true"><circle cx="8" cy="8" r="6.5" fill="none" stroke="#fff" stroke-width="1.5"/><path d="M1.5 8h13M8 1.5c-3 3.5-3 9.5 0 13M8 1.5c3 3.5 3 9.5 0 13" fill="none" stroke="#fff" stroke-width="1.2"/></svg>
        <span>www.Veralign.com</span>
      </li>
    </ul>
  </section>

</main>
</body>
</html>
```